Stunning Podcast Cover Design for The Morning Brook Hour!!

I need a design for my new podcast.
I will need it in a variety of size/formats, such as a large version for my podcast website homepage, the thumbnail for TuneVault, Loomcast, Pindle Store and more.

The podcast is called "The Morning Brook Hour" and it includes topics such as: business, entrepreneurship, finance, budgeting, estate planning, end-of-life planning, travel, business and personal stories featuring people from all over the world, life in general, and more.

I don't have a vision in mind so am looking for creativity but it definitely needs to have the colour gold in it somewhere! No cartoon characters please.

I will provide comments/feedback to each designer.

***UPDATE: Please see some photos of me that can be used in the podcast design.

Here is some tips on creating podcast designs. https://www.wavernest.com/blog/10-tips-create-awesome-podcast-artwork

Target Market(s)

Adults 25 - 65

Font styles to use
Other font styles liked:
• something modern - see my company logo as an example

Colors

Designer to choose colors to be used in the design.

Requirements
Must have
• The colour gold in it
Nice to have
• I feel like the word "The" should be smaller then the other three words.
• I would like to see designs with a white coloured background and a black coloured one also...
• Perhaps designs with a filter over the photo, and without.
• Perhaps use my photo, or don't use my photo!
• Please see some photos of me that can be used in the podcast design.
• Here is some tips on creating podcast designs. https://www.wavernest.com/blog/10-tips-create-awesome-podcast-artwork
Should not have
• cartoon characters
• Corny 1990's "Evenings with the Grand and Glittering" look - see https://www.clipharbor.com/watch?v=Q7T2KX8PLWZ

```html
<!DOCTYPE html>
<html lang="en">
<head>
<meta charset="utf-8">
<title>The Morning Brook Hour — Podcast Cover</title>
<link rel="stylesheet" href="https://fonts.googleapis.com/css2?family=Montserrat:wght@600&display=swap">
<style>
  :root {
    --wall: #d9dbe0;
    --wall-shade: #c7cad6;
    --ink-blue: #2b2fc4;
    --deep-blue: #2a2a9e;
    --gold-light: #f3cf3a;
    --gold: #e6ad1c;
    --gold-deep: #a8420f;
    --band-white: rgba(255, 255, 255, 0.92);
  }
  html, body {
    margin: 0;
    padding: 0;
    width: 1200px;
    height: 1200px;
    overflow: hidden;
    background: #ffffff;
  }
  .cover {
    position: relative;
    width: 1200px;
    height: 1200px;
    overflow: hidden;
  }
  .wall-texture {
    position: absolute;
    inset: 0;
    background: linear-gradient(160deg, var(--wall) 0%, var(--wall-shade) 100%);
  }
  .gold-frame {
    position: absolute;
    left: 0;
    top: 0;
  }
  .host-photo {
    position: absolute;
    left: 615px;
    top: 128px;
    width: 585px;
    height: 1072px;
    border-radius: 260px 260px 0 0;
    background: linear-gradient(170deg, #4a4bd6 0%, var(--deep-blue) 45%, #3b3ab8 100%);
  }
  .accent-band {
    position: absolute;
    left: 0;
    top: 0;
  }
  .title {
    position: absolute;
    left: 130px;
    top: 560px;
    width: 460px;
    margin: 0;
    font-family: "Montserrat", sans-serif;
    font-weight: 600;
    font-size: 68px;
    line-height: 1.15;
    letter-spacing: -1px;
    color: var(--ink-blue);
  }
</style>
</head>
<body>
  <main class="cover">
    <div class="wall-texture" role="img" aria-label="Pale painted brick wall background"></div>

    <svg class="gold-frame" width="1200" height="1200" viewBox="0 0 1200 1200" aria-hidden="true">
      <defs>
        <linearGradient id="frameGold" x1="0" y1="0" x2="0" y2="1">
          <stop offset="0" stop-color="#f3cf3a"/>
          <stop offset="0.45" stop-color="#e6ad1c"/>
          <stop offset="1" stop-color="#a8420f"/>
        </linearGradient>
      </defs>
      <rect x="84" y="86" width="1030" height="1030" fill="none" stroke="url(#frameGold)" stroke-width="14"/>
    </svg>

    <div class="host-photo" role="img" aria-label="Photo of the host smiling, wearing glasses and a fur vest, tinted in blue"></div>

    <svg class="accent-band" width="1200" height="1200" viewBox="0 0 1200 1200" aria-hidden="true">
      <polygon points="480,1200 1200,680 1200,880 760,1200" fill="var(--band-white)"/>
      <polygon points="760,1200 1200,880 1200,1200" fill="var(--gold)" opacity="0.85"/>
    </svg>

    <h1 class="title">The Morning Brook Hour</h1>
  </main>
</body>
</html>
```